Eid Mubarak Digital Graphic

We seek designs for a digital greeting wishing our clients an Eid Mubarak. The graphic can contain Arabic and English text. This digital greeting should include our company logo.

Target Market(s)

Clients both commercial and government

Industry/Entity Type

Consulting

Font styles to use
Serif
Sans Serif
Decorative
Script
Other font styles liked:
• Arabic calligraphy

Requirements
Must have
• Digital graphic in a format easily sent by email and text
Company logo
Traditional Arabic greeting
Original graphic, not copied
Nice to have
• Arabic calligraphy
Should not have
• Nothing offensive to the Islamic religion

```html
<!DOCTYPE html>
<html lang="en">
<head>
<meta charset="utf-8">
<title>Eid Mubarak Greeting</title>
<link rel="stylesheet" href="https://fonts.googleapis.com/css2?family=Aref+Ruqaa:wght@700&family=Caveat:wght@600&family=Domine:wght@400;700&family=Montserrat:wght@500;600&display=swap">
<style>
  :root {
    --bg-brown: #3a2209;
    --arch-rim: #2f1a0c;
    --arch-fill: #261309;
    --gold: #f4bf4a;
    --gold-light: #f8d676;
    --gold-deep: #c9912a;
    --white: #ffffff;
    --pill: #a58b63;
    --brand-orange: #ee7a2c;
    --band-tone: #3a230f;
  }
  * { margin: 0; padding: 0; box-sizing: border-box; }
  html, body { width: 1200px; height: 1200px; overflow: hidden; background: var(--bg-brown); }
  .greeting-card {
    position: relative;
    width: 1200px;
    height: 1200px;
    background: var(--bg-brown);
    overflow: hidden;
  }
  .arch-shape { position: absolute; inset: 0; width: 1200px; height: 1200px; }
  .lower-ornament-band {
    position: absolute;
    left: 0; bottom: 0;
    width: 1200px; height: 230px;
    background: linear-gradient(180deg, rgba(58,35,15,0) 0%, var(--band-tone) 55%, #3d2510 100%);
  }
  .brand-mark {
    position: absolute;
    top: 36px; right: 42px;
    display: flex;
    align-items: center;
    gap: 18px;
  }
  .brand-dot {
    width: 26px; height: 26px;
    border-radius: 50%;
    background: var(--brand-orange);
    flex: none;
  }
  .brand-name {
    font-family: "Domine", Georgia, serif;
    font-weight: 400;
    color: var(--brand-orange);
    font-size: 36px;
    line-height: 42px;
    letter-spacing: 1px;
    text-align: left;
  }
  .crescent-mosque-art {
    position: absolute;
    left: 422px; top: 250px;
    width: 356px; height: 305px;
    border-radius: 50%;
    background: radial-gradient(circle at 40% 40%, var(--gold-light) 0%, var(--gold) 50%, var(--gold-deep) 100%);
  }
  .headline {
    position: absolute;
    top: 592px; left: 0;
    width: 1200px;
    text-align: center;
    font-family: "Caveat", cursive;
    font-weight: 600;
    font-size: 132px;
    line-height: 140px;
    color: var(--gold);
  }
  .arabic-greeting {
    position: absolute;
    top: 736px; left: 0;
    width: 1200px;
    text-align center;
    text-align: center;
    font-family: "Aref Ruqaa", serif;
    font-weight: 700;
    font-size: 44px;
    line-height: 60px;
    color: var(--white);
  }
  .blessing {
    position: absolute;
    top: 838px; left: 0;
    width: 1200px;
    text-align: center;
    font-family: "Montserrat", Arial, sans-serif;
    font-weight: 500;
    font-size: 31px;
    line-height: 50px;
    color: var(--white);
  }
  .hijri-year {
    position: absolute;
    left: 409px; top: 1036px;
    width: 382px; height: 100px;
    border-radius: 50px;
    background: var(--pill);
    display: flex;
    align-items: center;
    justify-content: center;
    font-family: "Domine", Georgia, serif;
    font-weight: 700;
    font-size: 40px;
    letter-spacing: 4px;
    color: var(--white);
  }
</style>
</head>
<body>
  <main class="greeting-card">
    <svg class="arch-shape" viewBox="0 0 1200 1200" aria-hidden="true">
      <path fill="var(--arch-rim)" d="M600,62 C585,118 540,168 468,198 C396,228 322,250 292,320 C262,392 168,424 0,444 L0,1200 L1200,1200 L1200,444 C1032,424 938,392 908,320 C878,250 804,228 732,198 C660,168 615,118 600,62 Z"/>
      <path fill="var(--arch-fill)" d="M600,98 C586,146 544,190 476,218 C408,246 346,266 318,332 C290,402 192,440 0,460 L0,1200 L1200,1200 L1200,460 C1008,440 910,402 882,332 C854,266 792,246 724,218 C656,190 614,146 600,98 Z"/>
    </svg>
    <div class="lower-ornament-band" role="img" aria-label="Faint Arabic geometric ornament border"></div>

    <div class="brand-mark">
      <span class="brand-dot"></span>
      <div class="brand-name">Meridian<br>Advisory<br>Group LLC</div>
    </div>

    <div class="crescent-mosque-art" role="img" aria-label="Gold glitter crescent moon holding a mosque silhouette with domes and a minaret"></div>

    <h1 class="headline">Eid Mubarak</h1>
    <p class="arabic-greeting" lang="ar" dir="rtl">عيد مبارك</p>
    <p class="blessing">May Allah accept your fasts and prayers<br>and bless you and your loved ones<br>with peace and joy.</p>
    <div class="hijri-year">1442H</div>
  </main>
</body>
</html>
```